Harbourline Care Collective Needs a Pro business Card

Hello Everyone,
Harbourline Care Collective needs a awesome, neat, professional business card design
Colours: follows the logo of Red(maroon) and dark Grey
About the company.
Harbourline Care Collective is a company which house a "group" of allied health professionals including Physiotherapy, and eventually podiatry , speech pathology, psychology etc.
I am a physiotherapist by trade, and this company will start off heading towards and establishing its physiotherapy division first. (including the physiotherapy practice, mobile physiotherapy service etc).
Details for the logo,
- Double sided
- You may have the Harbourline Motion on the front and the back with Harbourline care collective/ a holistic approach to healthcare" tag line
- i am going to leave the design to you.
My details
Name: Colin Marsh
Physiotherapist
B AppSc (Phty)
Phone: 0491526037
fax: 9615 4078
Address: PO Box 5174 Kelvale NSW 2196
Email: physio@harbourlinecare.com.au
Web: www.harbourlinecare.com.au
Health

```html
<!DOCTYPE html>
<html lang="en">
<head>
<meta charset="utf-8">
<title>Harbourline Motion – Business Card</title>
<link href="https://fonts.googleapis.com/css2?family=Cinzel:wght@500&family=Cormorant+Garamond:ital,wght@1,500&family=Exo+2:wght@400;500&family=Oswald:wght@500&display=swap" rel="stylesheet">
<style>
  :root {
    --brand-red: #c4262e;
    --brand-dark: #2b2b2b;
    --paper: #ffffff;
    --backdrop: #e8e6e3;
    --ink-soft: #3a3a3a;
    --card-w: 800px;
    --card-h: 457px;
  }
  * { box-sizing: border-box; margin: 0; padding: 0; }
  html, body {
    width: 1200px;
    height: 1018px;
    overflow: hidden;
    background: var(--backdrop);
  }
  .card {
    position: absolute;
    left: 200px;
    width: var(--card-w);
    height: var(--card-h);
    background: var(--brand-red);
    overflow: hidden;
    box-shadow: 0 6px 18px rgba(0,0,0,0.18);
  }
  .card--front { top: 32px; }
  .card--back  { top: 529px; }

  .panel { position: absolute; inset: 0; }
  .panel--white {
    background: var(--paper);
    clip-path: polygon(0 0, 600px 0, 540px 228px, 0 228px);
  }
  .panel--dark {
    background: var(--brand-dark);
    clip-path: polygon(600px 0, 680px 0, 596px 320px, 0 320px, 0 228px, 540px 228px);
  }

  .brand {
    position: absolute;
    left: 64px;
    top: 78px;
  }
  .brand__name {
    display: flex;
    align-items: center;
    gap: 14px;
    font-family: "Cinzel", serif;
    font-weight: 500;
    font-size: 38px;
    color: var(--brand-red);
    letter-spacing: 1px;
  }
  .brand__square {
    width: 18px;
    height: 18px;
    background: var(--brand-red);
  }
  .brand__tagline {
    margin-top: 8px;
    margin-left: 32px;
    font-family: "Cormorant Garamond", serif;
    font-style: italic;
    font-weight: 500;
    font-size: 17px;
    color: var(--ink-soft);
  }

  .contacts {
    position: absolute;
    left: 44px;
    top: 244px;
    display: grid;
    grid-template-columns: 190px 300px;
    row-gap: 16px;
    column-gap: 20px;
    font-family: "Exo 2", sans-serif;
    font-size: 16px;
    color: var(--paper);
  }
  .contact {
    display: flex;
    align-items: center;
    gap: 10px;
  }
  .contact svg { width: 16px; height: 16px; flex: none; }

  .person {
    position: absolute;
    left: 44px;
    top: 340px;
    color: var(--paper);
  }
  .person__name {
    font-family: "Oswald", sans-serif;
    font-weight: 500;
    font-size: 36px;
    letter-spacing: 1px;
    line-height: 1;
    text-transform: uppercase;
  }
  .person__role,
  .person__credential {
    margin-top: 6px;
    font-family: "Exo 2", sans-serif;
    font-size: 16px;
    letter-spacing: 2px;
    line-height: 1.2;
  }
  .person__role { text-transform: uppercase; }

  .address {
    position: absolute;
    right: 30px;
    top: 40px;
    text-align: right;
    font-family: "Exo 2", sans-serif;
    font-weight: 500;
    font-size: 19px;
    line-height: 1.45;
    letter-spacing: 1px;
    color: var(--paper);
  }

  .back-band {
    position: absolute;
    inset: 0;
    background: var(--brand-dark);
    clip-path: polygon(150px 0, 260px 0, 200px 230px, 90px 230px);
  }
  .back-block {
    position: absolute;
    left: 470px;
    top: 250px;
    width: 180px;
    height: 150px;
    background: var(--brand-dark);
  }
  .back-brand {
    position: absolute;
    right: 44px;
    top: 80px;
    text-align: right;
    color: var(--paper);
  }
  .back-brand__name {
    font-family: "Cinzel", serif;
    font-weight: 500;
    font-size: 30px;
    letter-spacing: 1px;
  }
  .back-brand__tagline {
    margin-top: 8px;
    font-family: "Cormorant Garamond", serif;
    font-style: italic;
    font-weight: 500;
    font-size: 18px;
  }
</style>
</head>
<body>

<section class="card card--front" aria-label="Business card, front">
  <div class="panel panel--white"></div>
  <div class="panel panel--dark"></div>

  <div class="brand">
    <div class="brand__name"><span class="brand__square"></span>Harbourline Motion</div>
    <div class="brand__tagline">A Holistic Approach To Health Care</div>
  </div>

  <div class="contacts">
    <div class="contact">
      <svg viewBox="0 0 16 16" aria-hidden="true"><path fill="#fff" d="M3.6 1.5l2.2 2.6-1.3 1.6c.9 2 2.6 3.7 4.6 4.6l1.6-1.3 2.6 2.2-1.2 2.2C7 13 3 9 2 3.1z"/></svg>
      <span>0491526037</span>
    </div>
    <div class="contact">
      <svg viewBox="0 0 16 16" aria-hidden="true"><rect x="1.5" y="3.5" width="13" height="9" fill="none" stroke="#fff" stroke-width="1.4"/><path d="M1.5 3.5L8 9l6.5-5.5" fill="none" stroke="#fff" stroke-width="1.4"/></svg>
      <span>physio@harbourlinecare.com.au</span>
    </div>
    <div class="contact">
      <svg viewBox="0 0 16 16" aria-hidden="true"><rect x="4" y="1.5" width="8" height="13" rx="1.2" fill="none" stroke="#fff" stroke-width="1.4"/><circle cx="8" cy="12" r="0.9" fill="#fff"/></svg>
      <span>9615 4078</span>
    </div>
    <div class="contact">
      <svg viewBox="0 0 16 16" aria-hidden="true"><circle cx="8" cy="8" r="6.5" fill="none" stroke="#fff" stroke-width="1.3"/><ellipse cx="8" cy="8" rx="2.8" ry="6.5" fill="none" stroke="#fff" stroke-width="1.1"/><path d="M1.5 8h13M2.6 4.8h10.8M2.6 11.2h10.8" stroke="#fff" stroke-width="1"/></svg>
      <span>www.harbourlinecare.com.au</span>
    </div>
  </div>

  <div class="person">
    <div class="person__name">Colin Marsh</div>
    <div class="person__role">Physiotherapist</div>
    <div class="person__credential">B AppSc (Phty)</div>
  </div>

  <div class="address">
    PO Box 5174<br>
    Kelvale NSW 2196
  </div>
</section>

<section class="card card--back" aria-label="Business card, back">
  <div class="back-band"></div>
  <div class="back-block"></div>
  <div class="back-brand">
    <div class="back-brand__name">Harbourline Care Collective</div>
    <div class="back-brand__tagline">A Holistic Approach To Health Care</div>
  </div>
</section>

</body>
</html>
```